Body therapist needs a business card

I need a card for my business which is teaching trainings in body therapy, the company is called Wexcombe Educational Group. I teach to massage therapists around Australia, South East Asia and the USA. I am attaching my logo which will guide you as to what colours I would like to have you consider. Please consult my website to find out more about what I do. www.corvantela.com.au

My name is Daniel Wexcombe. My phone number is (03) 9417 2608 or 0461753208. email is info@corvantela.com.au

```html
<!DOCTYPE html>
<html lang="en">
<head>
<meta charset="utf-8">
<title>Wexcombe Educational Group – Business Card</title>
<link rel="stylesheet" href="https://fonts.googleapis.com/css2?family=Lato:wght@400;700&display=swap">
<style>
  :root {
    --stage: #2b2b2b;
    --card: #1c1d1f;
    --card-back: #1f2022;
    --pattern-tone: #2a2b2e;
    --brown: #8f4c12;
    --rust: #a55a17;
    --white: #f2f2f2;
    --rule: #6a6a6a;
  }
  * { box-sizing: border-box; margin: 0; padding: 0; }
  html, body { width: 1200px; height: 1108px; overflow: hidden; }
  body {
    background: var(--stage);
    font-family: "Lato", sans-serif;
    position: relative;
  }
  .card {
    position: absolute;
    top: 234px;
    width: 400px;
    height: 640px;
    border-radius: 22px;
    overflow: hidden;
  }
  .card--front { left: 160px; background: var(--card); }
  .card--back { left: 640px; background: var(--card-back); }

  .brand {
    position: absolute;
    top: 118px;
    left: 48px;
    display: flex;
    align-items: center;
    gap: 16px;
  }
  .brand__dot {
    width: 58px; height: 58px; border-radius: 50%;
    background: var(--brown);
    flex: none;
  }
  .brand__name {
    color: var(--brown);
    font-weight: 400;
    font-size: 25px;
    line-height: 1.15;
  }

  .person {
    position: absolute;
    top: 352px;
    width: 100%;
    text-align: center;
    color: var(--rust);
    font-weight: 700;
    font-size: 24px;
    letter-spacing: 0.5px;
    text-transform: uppercase;
  }
  .divider {
    position: absolute;
    top: 400px;
    left: 60px; right: 60px;
    display: flex;
    align-items: center;
    gap: 8px;
  }
  .divider__line { flex: 1; height: 1px; background: var(--rule); }
  .divider__icon {
    width: 26px; height: 26px; border-radius: 50%;
    background: var(--rust);
    display: flex; align-items: center; justify-content: center;
  }
  .contact {
    position: absolute;
    top: 440px;
    width: 100%;
    text-align: center;
    color: var(--white);
    font-size: 19px;
    line-height: 1.35;
  }
  .rule {
    position: absolute;
    top: 540px;
    left: 70px; right: 70px;
    height: 1px;
    background: var(--rule);
  }
  .address {
    position: absolute;
    top: 556px;
    width: 100%;
    text-align: center;
    color: var(--white);
    font-size: 19px;
    line-height: 1.3;
  }

  .back-field {
    position: absolute;
    inset: 0 0 150px 0;
    background: linear-gradient(180deg, var(--pattern-tone), var(--card-back));
  }
  .back-brand {
    position: absolute;
    top: 470px;
    width: 100%;
    display: flex;
    align-items: center;
    justify-content: center;
    gap: 10px;
  }
  .back-brand__dot { width: 26px; height: 26px; border-radius: 50%; background: var(--brown); }
  .back-brand__name { color: var(--brown); font-size: 16px; }
</style>
</head>
<body>
  <section class="card card--front" aria-label="Business card front">
    <div class="brand">
      <span class="brand__dot"></span>
      <span class="brand__name">Wexcombe<br>Educational Group</span>
    </div>

    <p class="person">Daniel Wexcombe</p>

    <div class="divider">
      <span class="divider__line"></span>
      <span class="divider__icon">
        <svg width="14" height="14" viewBox="0 0 24 24" aria-hidden="true"><path fill="#1c1d1f" d="M6.6 10.8a15 15 0 0 0 6.6 6.6l2.2-2.2c.3-.3.7-.4 1-.2 1.1.4 2.3.6 3.6.6.6 0 1 .4 1 1V20c0 .6-.4 1-1 1A17 17 0 0 1 3 4c0-.6.4-1 1-1h3.5c.6 0 1 .4 1 1 0 1.3.2 2.5.6 3.6.1.3 0 .7-.2 1z"/></svg>
      </span>
      <span class="divider__icon">
        <svg width="14" height="14" viewBox="0 0 24 24" aria-hidden="true"><rect x="3" y="6" width="18" height="12" rx="1" fill="#1c1d1f"/><path d="M3 7l9 6 9-6" stroke="#a55a17" stroke-width="1.6" fill="none"/></svg>
      </span>
      <span class="divider__icon">
        <svg width="14" height="14" viewBox="0 0 24 24" aria-hidden="true"><circle cx="12" cy="12" r="9" fill="none" stroke="#1c1d1f" stroke-width="2.2"/><path d="M3 12h18M12 3c3 3 3 15 0 18M12 3c-3 3-3 15 0 18" stroke="#1c1d1f" stroke-width="1.6" fill="none"/></svg>
      </span>
      <span class="divider__line"></span>
    </div>

    <p class="contact">+61 (03) 9417 2608<br>info@corvantela.com.au<br>www.corvantela.com.au</p>
    <div class="rule"></div>
    <p class="address">P.O. Box 2847, Larwood East<br>Victoria, 3189 Australia</p>
  </section>

  <section class="card card--back" aria-label="Business card back">
    <div class="back-field" role="img" aria-label="Faint repeating brand pattern in dark grey"></div>
    <div class="back-brand">
      <span class="back-brand__dot"></span>
      <span class="back-brand__name">Wexcombe Educational Group</span>
    </div>
  </section>
</body>
</html>
```